Northfield Server Crate requires an Email Marketing Design template

Northfield Server Crate are a rapidly expanding UK based internet hosting company that have just re-branded through Craft Lantern.
We provide internet based services such as website hosting, dedicated and managed servers, domain names as well as email solutions to name a few. We pride ourselves on being able to provide a comprehensive, secure, future proofed and scalable platform for our clients to communicate and do business on.
Northfield Server Crate are looking to go live with a new website on 1st August. In preparation for this we would like to have an HTML Email Template designed for our launch!
We are also having a really big push on the reseller market allowing potential resellers and their end users to manage their own services via a consolidated portal with many features and functions that will grow over time.

Target Market(s)
We have 3 core target markets, the end user who would be the likes of web designers or developers. A reseller market who would want to resell our hosted services and the final target market would be a business client that would want high end server and hosting solutions.
Industry/Entity Type
Internet Service Provider
Requirements
Must have
- To ensure it is inline with the new brand (see attached files).

```html
<!DOCTYPE html>
<html lang="en">
<head>
<meta charset="utf-8">
<title>Northfield Server Crate – Launch Email</title>
<link rel="stylesheet" href="https://fonts.googleapis.com/css2?family=Oswald:wght@500;700&family=Open+Sans:wght@400;600;700&display=swap">
<style>
:root{
  --page:#efefef;
  --ink:#2b2b2b;
  --ink-soft:#555;
  --white:#ffffff;
  --grey-band:#cdcdcd;
  --charcoal:#333638;
  --green:#7cc8a1;
  --mint:#dcf3e7;
  --teal:#2dbdb5;
  --teal-dark:#23494a;
  --yellow:#f4d94b;
  --olive:#3b3520;
  --navy:#27578a;
  --navy-deep:#1f4673;
  --slate:#2e3337;
  --red:#e3463c;
  --gear:#8b9096;
  --card-blue:#3d7fc4;
  --head:"Oswald", "Arial Narrow", sans-serif;
  --body:"Open Sans", Arial, sans-serif;
}
*{box-sizing:border-box;margin:0;padding:0}
html,body{width:1200px;height:4000px;overflow:hidden;background:var(--page);font-family:var(--body);color:var(--ink)}
.email{position:absolute;left:120px;top:0;width:960px}
.photo{position:absolute}

/* header */
.hero{position:relative;height:580px;background:linear-gradient(180deg,#fafafa,#f1f1f1)}
.brand{position:absolute;left:0;top:60px;display:flex;align-items:center;gap:16px}
.brand-dot{width:52px;height:52px;border-radius:50%;background:var(--teal)}
.brand-name{font-family:var(--body);font-weight:700;font-size:26px;color:var(--ink);line-height:1.1;width:220px}
.social{position:absolute;right:40px;top:74px;display:flex;gap:26px}
.social span{width:26px;height:26px;border-radius:50%;background:#c4c4c4}
.hero-photo{right:0;top:30px;width:380px;height:550px;background:linear-gradient(160deg,#f7f3ee 0%,#e9ded2 55%,#d8c3ad 100%)}
.hero-title{position:absolute;left:0;top:245px;font-family:var(--head);font-weight:700;font-size:74px;line-height:76px;letter-spacing:1px;color:var(--ink)}
.hero-sub{position:absolute;left:0;top:412px;width:330px;font-size:22px;line-height:30px;color:var(--ink-soft)}

/* bands */
.band{display:flex;align-items:center;padding-left:0;font-family:var(--head);font-weight:700;text-transform:uppercase}
.band-tagline{height:100px;background:var(--grey-band);font-size:42px;color:var(--ink);padding-left:0}
.band-tagline span{padding-left:0}
.pitch{height:340px;background:var(--charcoal);color:var(--white);padding:70px 40px 0 40px}
.pitch h2{font-family:var(--head);font-weight:700;font-size:58px;line-height:64px}
.pitch p{margin-top:20px;font-size:22px;line-height:31px;color:#e6e6e6}
.band-plans{height:80px;background:var(--green);color:var(--white);font-size:34px;padding-left:40px}

/* plan rows */
.plan{position:relative;display:flex}
.plan-info{padding:0 34px}
.plan-info h3{font-family:var(--body);font-weight:700;font-size:32px;line-height:38px}
.plan-info .lede{margin-top:18px;font-size:17px;line-height:24px}
.plan-info .from{margin-top:44px;font-size:18px}
.plan-info .price{font-family:var(--head);font-weight:500;font-size:60px;line-height:66px}
.plan-info .price small{font-family:var(--body);font-size:16px;font-weight:400}
.btn{display:inline-block;margin-top:30px;padding:14px 28px;font-family:var(--body);font-weight:700;font-size:20px;text-transform:uppercase;color:var(--white)}

.plan-shared{height:620px}
.plan-shared .plan-info{width:300px;background:var(--mint);padding-top:150px}
.plan-shared .lede,.plan-shared .from{color:#6d9b84}
.plan-shared .price{color:var(--green)}
.plan-shared .btn{background:var(--green)}
.plan-shared .photo{position:static;width:660px;background:linear-gradient(135deg,#dfe8ee 0%,#9bb6c7 45%,#6c8aa0 100%)}

.plan-dedicated{height:600px}
.plan-dedicated .photo{position:static;width:640px;background:linear-gradient(120deg,#cfd7de 0%,#a46a4e 55%,#6a3d2c 100%)}
.plan-dedicated .plan-info{width:320px;background:var(--teal);color:var(--white);padding-top:140px}
.plan-dedicated .lede,.plan-dedicated .from{color:#d6f4f2}
.plan-dedicated .btn{background:var(--teal-dark)}

.plan-managed{height:612px}
.plan-managed .plan-info{width:360px;background:var(--yellow);color:var(--ink);padding-top:100px}
.plan-managed .btn{background:var(--olive)}
.plan-managed .photo{position:static;width:600px;background:linear-gradient(120deg,#5b6a78 0%,#c9cdd1 55%,#eef0f1 100%)}

/* promo */
.promo{height:120px;background:var(--navy);color:var(--white);text-align:center;padding-top:18px}
.promo h2{font-family:var(--head);font-weight:700;font-size:44px;line-height:52px;text-transform:uppercase}
.promo p{font-size:16px;color:#c9d8ea}

/* trust */
.trust{display:flex;height:348px}
.trust-copy{width:480px;background:var(--slate);color:var(--white);padding:60px 40px 0 40px}
.trust-copy h2{font-family:var(--head);font-weight:700;font-size:60px;line-height:60px;text-transform:uppercase}
.trust-copy p{margin-top:18px;font-size:22px;line-height:30px;color:#dcdcdc}
.trust .photo{position:static;width:480px;background:linear-gradient(110deg,#eef2f4 0%,#c7d3da 60%,#8d6f5d 100%)}

/* features */
.features{display:flex;height:320px;background:var(--white);padding:40px 16px 0}
.feature{flex:1;text-align:center;padding:0 18px}
.feature svg{width:64px;height:64px}
.feature h4{margin-top:12px;font-weight:700;font-size:22px;line-height:26px;color:var(--ink)}
.feature p{margin-top:12px;font-size:14px;line-height:19px;color:var(--ink-soft)}

/* footer */
.footer{position:relative;height:220px;background:linear-gradient(180deg,var(--navy),var(--navy-deep));color:var(--white);padding:44px 40px 0}
.footer h5{font-weight:700;font-size:22px;text-transform:uppercase}
.footer .about{margin-top:8px;width:440px;font-size:14px;line-height:20px;color:#c6d5e7}
.footer .contact{margin-top:18px;font-size:14px;line-height:22px;color:#c6d5e7}
.footer .view-online{position:absolute;right:40px;top:44px;text-align:right;font-weight:700;font-size:20px;line-height:26px}
</style>
</head>
<body>
<main class="email">

  <header class="hero">
    <div class="brand">
      <span class="brand-dot"></span>
      <span class="brand-name">Northfield Server Crate</span>
    </div>
    <div class="photo hero-photo" role="img" aria-label="Photo of a smiling woman at a laptop in a bright office with shelves"></div>
    <nav class="social" aria-label="Social links"><span></span><span></span><span></span></nav>
    <h1 class="hero-title">WEB HOSTING<br>MADE EASY.</h1>
    <p class="hero-sub">Hassle-free web hosting to start your online adventure now.</p>
  </header>

  <div class="band band-tagline"><span style="padding-left:0">&nbsp;FAST, SECURE AND RELIABLE.</span></div>

  <section class="pitch">
    <h2>PAY LESS. GET MORE.</h2>
    <p>Build your fast, secure and reliable Server Crate. Whether you are trying to start an online business, share your stories on a blog or sell products.. your Crate understands all your hosting needs.</p>
  </section>

  <div class="band band-plans">CHOOSE YOUR PERFECT HOSTING PLAN.</div>

  <section class="plan plan-shared">
    <div class="plan-info">
      <h3>Shared Web Hosting</h3>
      <p class="lede">Suitable for individuals and small businesses</p>
      <p class="from">Starting at</p>
      <p class="price">£3.99<small>/month</small></p>
      <span class="btn">Know more</span>
    </div>
    <div class="photo" role="img" aria-label="Photo of four young people smiling around a computer"></div>
  </section>

  <section class="plan plan-dedicated">
    <div class="photo" role="img" aria-label="Photo of a man relaxing with hands behind his head in front of a brick wall"></div>
    <div class="plan-info">
      <h3>Dedicated Servers</h3>
      <p class="lede">Your best choice for high-traffic and resource-intensive sites for complete control.</p>
      <p class="from">Starting at</p>
      <p class="price">£127.99<small>/month</small></p>
      <span class="btn">Know more</span>
    </div>
  </section>

  <section class="plan plan-managed">
    <div class="plan-info">
      <h3>Dedicated Servers</h3>
      <p class="lede">Your best choice for high-traffic and resource-intensive sites for complete control.</p>
      <p class="from">Starting at</p>
      <p class="price">£16.97<small>/month</small></p>
      <span class="btn">Know more</span>
    </div>
    <div class="photo" role="img" aria-label="Photo of a man working on a laptop at an office desk"></div>
  </section>

  <section class="promo">
    <h2>Enjoy 30% off new purchases.</h2>
    <p>Use promo code CRATE30 in your cart when you order. Expires June 30, 2015.</p>
  </section>

  <section class="trust">
    <div class="trust-copy">
      <h2>Why<br>trust us?</h2>
      <p>Northfield Server Crate is effective cost, easy for novices, suitable for experts, and has..</p>
    </div>
    <div class="photo" role="img" aria-label="Photo of a smiling woman wearing a headset"></div>
  </section>

  <section class="features">
    <div class="feature">
      <svg viewBox="0 0 64 64" aria-hidden="true"><rect x="12" y="6" width="40" height="52" rx="3" fill="#5bb86a"/><rect x="20" y="18" width="24" height="4" fill="#fff"/><rect x="20" y="28" width="24" height="4" fill="#fff"/><rect x="20" y="38" width="16" height="4" fill="#fff"/></svg>
      <h4>Best value domain names</h4>
      <p>Instant domain registration of over 50 types of domains from around the world</p>
    </div>
    <div class="feature">
      <svg viewBox="0 0 64 64" aria-hidden="true"><circle cx="32" cy="32" r="26" fill="var(--red)"/><circle cx="32" cy="32" r="12" fill="#fff"/><rect x="29" y="6" width="6" height="14" fill="#fff"/><rect x="29" y="44" width="6" height="14" fill="#fff"/><rect x="6" y="29" width="14" height="6" fill="#fff"/><rect x="44" y="29" width="14" height="6" fill="#fff"/></svg>
      <h4>24/7<br>Free support</h4>
      <p>If you have questions, our team have the answers to help when you need it. Anytime.</p>
    </div>
    <div class="feature">
      <svg viewBox="0 0 64 64" aria-hidden="true"><g fill="var(--gear)"><rect x="28" y="4" width="8" height="56"/><rect x="4" y="28" width="56" height="8"/><rect x="28" y="4" width="8" height="56" transform="rotate(45 32 32)"/><rect x="28" y="4" width="8" height="56" transform="rotate(-45 32 32)"/><circle cx="32" cy="32" r="20"/></g><circle cx="32" cy="32" r="8" fill="#fff"/></svg>
      <h4>Free<br>migration</h4>
      <p>Free of charge service to migrate one or all your servers to our hosting platform.</p>
    </div>
    <div class="feature">
      <svg viewBox="0 0 64 64" aria-hidden="true"><rect x="4" y="14" width="56" height="36" rx="4" fill="var(--card-blue)"/><rect x="4" y="22" width="56" height="7" fill="#1f3f66"/><rect x="12" y="38" width="18" height="4" fill="#fff"/></svg>
      <h4>No hidden<br>charges</h4>
      <p>Fully inclusive with everything clearly stated in our plans with no hidden extras.</p>
    </div>
  </section>

  <footer class="footer">
    <h5>Northfield Server Crate</h5>
    <p class="about">Reliable hosting, domains and servers for designers, resellers and growing businesses across the UK.</p>
    <p class="contact">14 Harbour Lane, Leeds LS1 4AB<br>0113 496 0700</p>
    <p class="view-online">Can't read this E-mail?<br>Please click here</p>
  </footer>

</main>
</body>
</html>
```